Tarjetas de visita para empresa de aluminio

Empresa con mas de 40 años vendiendo perfiles de aluminio.
Somos fábrica y almacén, queremos renovar la tarjeta de presentación de nuestros comerciales dando una imgen innovadora y tecnógica mezclado con la calidez del respeto al medio ambiente.
Añado el logo de la empresa y actual cara trasera de la tarjeta de visita, el logo es el simbolo WM y la marca TRAVENIC EXTRUSION, la frase 2extrusion y lacado de aluminio" debe cambiarse por "Diseño, extrusión, lacado, anodizado y mecanizado de precisión de aluminio" o en su defecto incluir todos esos servicios que hacemos o una frase mas pegadiza.

We are an aluminium factory, we produce and stock profiles of aluminium.
we want to renew visit card of our sellers, we are looking for something that show innovation, tecnology and environment respect.
Upload our actual logo and back of visit card, logo WM and brand TRAVENIC EXTRUSION must be keept.
Text "Extrusion y lacado de aluminio" must be changed for "Diseño, extrusion, lacado, anodizado y mecanizado de precisión de aluminio" or something like that

```html
<!DOCTYPE html>
<html lang="es">
<head>
<meta charset="utf-8">
<title>Tarjetas de visita — Travenic Extrusion</title>
<link rel="stylesheet" href="https://fonts.googleapis.com/css2?family=Montserrat:wght@400;600;700&family=Michroma&display=swap">
<style>
  :root {
    --navy: #242d3d;
    --green: #6ab92f;
    --paper: #f2f2f2;
    --white: #ffffff;
    --backdrop: #e6e6e3;
    --line: rgba(255,255,255,0.35);
  }
  * { margin: 0; padding: 0; box-sizing: border-box; }
  html, body { width: 961px; height: 1200px; overflow: hidden; }
  body {
    background: var(--backdrop);
    font-family: "Montserrat", sans-serif;
    position: relative;
  }
  .card {
    position: absolute;
    left: 146px;
    width: 669px;
    height: 433px;
    background: var(--navy);
    overflow: hidden;
    box-shadow: 0 10px 24px rgba(0,0,0,0.25);
  }
  .card--front { top: 126px; }
  .card--back { top: 641px; }
  .bands { position: absolute; inset: 0; width: 669px; height: 433px; }

  /* Front */
  .brand-mark {
    position: absolute;
    display: flex; align-items: center; justify-content: center; gap: 14px;
    color: var(--white);
    font-family: "Michroma", sans-serif;
  }
  .card--front .brand-mark { left: 0; right: 0; top: 140px; font-size: 56px; }
  .brand-mark .dot {
    width: 18px; height: 18px; border-radius: 50%; background: var(--white);
  }
  .brand-name {
    position: absolute; left: 0; right: 0; text-align: center;
    color: var(--white);
    font-family: "Michroma", sans-serif;
    white-space: nowrap;
  }
  .card--front .brand-name { top: 246px; font-size: 27px; letter-spacing: 1px; }
  .tagline {
    position: absolute; text-align: center; color: var(--white);
    font-weight: 400; text-transform: uppercase;
  }
  .card--front .tagline { left: 0; right: 0; top: 290px; font-size: 13.5px; line-height: 20px; }

  /* Back */
  .card--back .brand-mark { left: 22px; width: 242px; top: 34px; font-size: 30px; gap: 9px; }
  .card--back .brand-mark .dot { width: 10px; height: 10px; }
  .card--back .brand-name { left: 22px; width: 242px; top: 99px; font-size: 14.5px; letter-spacing: 0.5px; }
  .card--back .tagline { left: 22px; width: 242px; top: 127px; font-size: 8.2px; line-height: 12.5px; }
  .network {
    position: absolute;
    background: linear-gradient(180deg, rgba(255,255,255,0.08), rgba(255,255,255,0.16), rgba(255,255,255,0.06));
  }
  .network--top { left: 383px; top: 0; width: 120px; height: 143px; }
  .network--bottom { left: 366px; top: 286px; width: 84px; height: 147px; }
  .holder {
    position: absolute; left: 0; right: 0; top: 168px; height: 104px;
    text-align: center; color: var(--navy);
  }
  .holder-name {
    margin-top: 26px;
    font-family: "Michroma", sans-serif; font-size: 25px; font-weight: 400;
    -webkit-text-stroke: 0.8px var(--navy);
    letter-spacing: 0.5px;
  }
  .holder-role {
    margin-top: 6px;
    font-family: "Michroma", sans-serif; font-size: 12px;
    letter-spacing: 13px; padding-left: 13px;
  }
  .contact {
    position: absolute; top: 322px;
    color: var(--white); font-weight: 600; font-size: 15.5px; line-height: 18.3px;
    white-space: nowrap;
  }
  .contact--address { left: 30px; }
  .contact--phones { right: 29px; text-align: right; }
</style>
</head>
<body>

<section class="card card--front">
  <svg class="bands" viewBox="0 0 669 433" aria-hidden="true">
    <polygon points="0,0 483,0 464,19 0,19" fill="var(--paper)"/>
    <polygon points="0,19 372,19 345,44 0,44" fill="var(--green)"/>
    <polygon points="323,390 669,390 669,415 297,415" fill="var(--green)"/>
    <polygon points="204,415 669,415 669,433 185,433" fill="var(--paper)"/>
  </svg>
  <div class="brand-mark"><span class="dot"></span><span>WM</span></div>
  <h1 class="brand-name">TRAVENIC EXTRUSION</h1>
  <p class="tagline">Diseño, extrusion, lacado, anodizado y<br>mecanizado de precisión de aluminio.</p>
</section>

<section class="card card--back">
  <svg class="bands" viewBox="0 0 669 433" aria-hidden="true">
    <polygon points="362,143 669,143 669,168 335,168" fill="var(--green)"/>
    <rect x="0" y="168" width="669" height="104" fill="var(--paper)"/>
    <polygon points="0,272 250,272 236,286 0,286" fill="var(--green)"/>
  </svg>
  <div class="network network--top" role="img" aria-label="Patrón decorativo de red de nodos y líneas finas"></div>
  <div class="network network--bottom" role="img" aria-label="Patrón decorativo de red de nodos y líneas finas"></div>
  <div class="brand-mark"><span class="dot"></span><span>WM</span></div>
  <h2 class="brand-name">TRAVENIC EXTRUSION</h2>
  <p class="tagline">Diseño, extrusion, lacado, anodizado y<br>mecanizado de precisión de aluminio.</p>
  <div class="holder">
    <p class="holder-name">MARCOS ORTEGA RUIZ</p>
    <p class="holder-role">COMERCIAL</p>
  </div>
  <address class="contact contact--address" style="font-style:normal">
    Pol. Ind. Los Olivos - C/4 N 22<br>
    41720 VILLAREAL DEL CAMPO (Sevilla)<br>
    Apartado de Correos 245<br>
    E-mail : marcosortega@travenic.com
  </address>
  <p class="contact contact--phones">
    Movil : 600 12 34 56<br>
    Telf : 955 00 11 22<br>
    Fax : 955 00 11 33<br>
    www.travenic.com
  </p>
</section>

</body>
</html>
```